Existing WP site needs a fresh look (design only)

The current website, www.tarnbelle.com.au, is fine, but needs a fresh look so their clients can tell their website has been 'refreshed' regularly.
https://www.tarnbelle.com.au/sitemap/
They will use the existing functionality.
They want to keep the blue, green and white of their logo as the main colors, but a fresh look. They prefer a light look to a dark look, but they would be open to good designs that change their mind.
Be creative, think outside the box.
You only need to supply the 'home page ' design to win but the winners will be asked to provide an extra 'standard' page template (like the one currently being used for search results and other pages)
Any photos used must be supplied without charge with the PSDs in a resolution acceptable for the WordPress site.
2 page

```html
<!DOCTYPE html>
<html lang="en">
<head>
<meta charset="utf-8">
<title>Tarnbelle Voices – Home</title>
<link rel="stylesheet" href="https://fonts.googleapis.com/css2?family=Montserrat:wght@500;600;700;800&family=Lato:wght@400;700&display=swap">
<style>
:root{
  --navy:#0b1640;
  --navy-deep:#060d2b;
  --blue:#1d2f8f;
  --green:#6cbf1f;
  --green-dark:#2f6e0a;
  --white:#ffffff;
  --ink:#1b1b1b;
  --grey:#8a8f99;
  --line:#d9dce3;
  --head:"Montserrat",Arial,sans-serif;
  --body:"Lato",Arial,sans-serif;
}
*{box-sizing:border-box;margin:0;padding:0}
html,body{width:1200px;height:3800px;overflow:hidden;background:var(--white)}
body{position:relative;font-family:var(--body);color:var(--ink)}

.hero{position:absolute;left:0;top:0;width:1200px;height:660px;border-radius:0 0 110px 110px;overflow:hidden;
  background:
    radial-gradient(ellipse 260px 300px at 640px 230px,rgba(40,30,60,.85) 0%,rgba(40,30,60,.4) 45%,rgba(40,30,60,0) 75%),
    radial-gradient(ellipse 320px 360px at 960px 320px,#c4183c 0%,rgba(196,24,60,.55) 45%,rgba(196,24,60,0) 80%),
    radial-gradient(ellipse 300px 260px at 420px 200px,#3a2aa8 0%,rgba(58,42,168,0) 75%),
    linear-gradient(100deg,#13208a 0%,#1f1f8e 35%,#3a1a7c 60%,#7a1650 85%,#a5123a 100%)}
.hero::after{content:"";position:absolute;left:0;right:0;bottom:0;height:260px;background:linear-gradient(180deg,rgba(10,10,50,0),rgba(10,10,50,.45))}
.topbar{position:absolute;top:0;left:0;right:0;height:110px;z-index:2}
.logo{position:absolute;left:120px;top:14px;display:flex;align-items:center;gap:10px}
.logo-square{width:20px;height:20px;background:var(--green);border-radius:3px}
.logo-name{font-family:var(--head);font-weight:800;font-size:28px;color:var(--white);line-height:1}
.phones{position:absolute;right:120px;top:22px;font-family:var(--head);font-weight:700;font-size:12px;color:var(--white);display:flex;align-items:center;gap:8px}
.phones .dot{width:16px;height:16px;border-radius:50%;background:var(--green)}
.nav{position:absolute;right:120px;top:88px;display:flex;gap:26px;font-family:var(--head);font-weight:600;font-size:11px;color:var(--white);letter-spacing:.5px}
.nav .active{border-bottom:2px solid var(--green);padding-bottom:4px}
.hero-title{position:absolute;top:320px;left:0;right:0;text-align:center;color:var(--white);font-family:var(--head);font-weight:800;font-size:58px;letter-spacing:1px;z-index:2}
.hero-title span{color:var(--green)}
.hero-sub{position:absolute;top:400px;left:0;right:0;text-align:center;color:var(--white);font-family:var(--head);font-weight:700;font-size:32px;z-index:2}

.search{position:absolute;left:140px;top:560px;width:920px;height:500px;background:var(--white);border-radius:60px 60px 0 0}
.section-title{font-family:var(--head);font-weight:700;font-size:40px;color:var(--ink);text-align:center;letter-spacing:.5px}
.search .section-title{margin-top:50px}
.fields{position:absolute;left:48px;top:150px;width:824px;display:grid;grid-template-columns:repeat(3,232px);justify-content:space-between;row-gap:44px}
.field{height:40px;border:1px solid var(--line);border-radius:3px;display:flex;align-items:center;justify-content:space-between;padding:0 14px;font-size:12px;color:#444;box-shadow:0 1px 3px rgba(0,0,0,.08)}
.field i{width:0;height:0;border-left:5px solid transparent;border-right:5px solid transparent;border-top:6px solid #333}
.btn{position:absolute;left:50%;transform:translateX(-50%);background:var(--green);color:var(--white);font-family:var(--head);font-weight:700;font-size:15px;border-radius:30px;width:200px;height:60px;display:flex;align-items:center;justify-content:center;letter-spacing:.5px}
.search .btn{top:320px}

.spot-title{position:absolute;top:1146px;left:0;right:0}
.spots{position:absolute;top:1248px;left:140px;width:920px;display:flex;gap:20px}
.spot{flex:1;height:216px;border-radius:70px 20px 70px 20px;position:relative;overflow:hidden}
.spot.one{background:radial-gradient(circle at 50% 45%,#f3d2b8 0%,#e6b48f 22%,rgba(230,180,143,0) 45%),linear-gradient(135deg,#4f9be0,#2a6fc0 60%,#1c3d8a)}
.spot.two{background:radial-gradient(circle at 50% 45%,#b7876a 0%,#7a5240 25%,rgba(122,82,64,0) 50%),linear-gradient(135deg,#2a2a2a,#0c0c0c)}
.spot.three{background:radial-gradient(circle at 55% 50%,#e8c3a4 0%,#c89a78 25%,rgba(200,154,120,0) 50%),linear-gradient(135deg,#e9d2a0,#6b5a55 60%,#2a2c44)}
.play{position:absolute;left:50%;top:50%;width:64px;height:64px;margin:-32px 0 0 -32px}
.spots-btn{top:1514px}

.clients{position:absolute;top:1660px;left:0;width:1200px;height:220px;background:linear-gradient(90deg,var(--navy),var(--blue) 50%,var(--navy));border-radius:110px}
.clients .section-title{color:var(--white);margin-top:48px}
.logos{position:absolute;top:122px;left:150px;right:150px;display:flex;justify-content:space-between;align-items:center;font-family:var(--head);font-weight:700;font-size:22px;color:var(--white)}
.logos span{display:flex;align-items:center;gap:8px}
.logos .sq{width:16px;height:16px;background:var(--white)}
.arrow{position:absolute;top:120px;width:24px;height:30px}

.news-title{position:absolute;top:2044px;left:0;right:0}
.news{position:absolute;top:2140px;left:140px;width:920px;display:flex;gap:24px}
.card{flex:1;background:var(--white);box-shadow:0 4px 24px rgba(0,0,0,.12);border-radius:50px 50px 0 0;height:520px;position:relative}
.card-img{height:260px;border-radius:50px 50px 0 0}
.card-img.a{background:radial-gradient(ellipse 130px 170px at 50% 55%,#cfcfcf 0%,#9a9a9a 45%,rgba(154,154,154,0) 80%),linear-gradient(160deg,#e4e4e4,#3d3d3d)}
.card-img.b{background:radial-gradient(ellipse 130px 160px at 50% 55%,#c49a80 0%,#8e6650 45%,rgba(142,102,80,0) 80%),linear-gradient(160deg,#505050,#1e1e1e)}
.card-body{padding:28px 22px}
.meta{font-size:11px;color:var(--grey)}
.card h3{font-family:var(--head);font-weight:700;font-size:14px;margin:14px 0 14px}
.card p{font-size:12px;line-height:1.7;color:#777}
.more{position:absolute;left:22px;bottom:28px;font-family:var(--head);font-weight:700;font-size:13px;color:var(--green)}
.news-btn{top:2702px}

.testimonials{position:absolute;top:2820px;left:0;width:1200px;height:760px;border-radius:160px 160px 0 0;overflow:hidden;
  background:linear-gradient(90deg,#0b2604 0%,#245f0a 40%,#4f9e16 70%,var(--green) 100%)}
.mic-photo{position:absolute;left:0;top:0;width:700px;height:760px;
  background:
    radial-gradient(ellipse 170px 120px at 330px 150px,#b9f06a 0%,#7cc92a 40%,rgba(124,201,42,0) 80%),
    radial-gradient(ellipse 260px 320px at 300px 380px,#4a9a14 0%,rgba(74,154,20,.5) 50%,rgba(74,154,20,0) 85%),
    linear-gradient(180deg,rgba(5,20,2,.2),rgba(5,20,2,.75))}
.t-body{position:absolute;left:640px;top:120px;width:440px;color:var(--white)}
.t-body h2{font-family:var(--head);font-weight:800;font-size:46px;letter-spacing:.5px}
.t-body blockquote{font-family:var(--head);font-weight:600;font-style:italic;font-size:19px;line-height:1.55;margin-top:20px}
.t-author{display:flex;gap:16px;align-items:center;margin-top:28px}
.t-badge{width:64px;height:60px;background:var(--white)}
.t-author strong{font-family:var(--head);font-size:17px;display:block}
.t-author small{font-size:12px;font-style:italic}
.t-arrows{position:absolute;left:650px;top:500px;display:flex;gap:10px}
.t-arrows span{width:32px;height:32px;border-radius:50%;border:2px solid var(--white);display:flex;align-items:center;justify-content:center}

.footer{position:absolute;top:3580px;left:0;width:1200px;height:220px;background:var(--navy-deep);color:var(--white)}
.f-col{position:absolute;top:30px;display:flex;gap:18px;align-items:center;font-size:11px;line-height:1.6}
.f-icon{width:56px;height:56px;border-radius:50%;background:var(--green);display:flex;align-items:center;justify-content:center}
.f-links{position:absolute;top:120px;left:0;right:0;text-align:center;font-family:var(--head);font-weight:600;font-size:12px;letter-spacing:.5px;line-height:2.1}
.f-copy{position:absolute;top:188px;left:0;right:0;text-align:center;font-size:10px;color:#b7bdd0}
.to-top{position:absolute;right:40px;top:160px;width:30px;height:30px;border-radius:50%;background:var(--green);display:flex;align-items:center;justify-content:center}
</style>
</head>
<body>
<header class="hero" role="img" aria-label="Singer performing into a studio microphone in blue and crimson light">
  <div class="topbar">
    <div class="logo"><div class="logo-square"></div><div class="logo-name">Tarnbelle Voices</div></div>
    <div class="phones"><span class="dot"></span>SYDNEY +61 2 9000 4812 | MELBOURNE +61 3 9000 2367</div>
    <nav class="nav"><span class="active">HOME</span><span>VOICES</span><span>RATES</span><span>PAYMENTS</span><span>NEWS</span><span>ABOUT US</span><span>CLIENTS</span><span>MORE</span></nav>
  </div>
  <h1 class="hero-title">AUSTRALIA'S <span>TOP VOICES</span></h1>
  <p class="hero-sub">PROFESSIONAL CASTING</p>
</header>

<section class="search">
  <h2 class="section-title">SEARCH ARTISTS</h2>
  <div class="fields">
    <div class="field">Location<i></i></div>
    <div class="field">Sex<i></i></div>
    <div class="field">Age Range<i></i></div>
    <div class="field">Talent Range<i></i></div>
    <div class="field">Language<i></i></div>
    <div class="field">Accent<i></i></div>
  </div>
  <div class="btn">SEARCH</div>
</section>

<h2 class="section-title spot-title">SPOTLIGHTS</h2>
<section class="spots">
  <div class="spot one" role="img" aria-label="Video still of a young voice artist">
    <svg class="play" viewBox="0 0 64 64"><circle cx="32" cy="32" r="30" fill="rgba(0,0,0,.25)" stroke="#fff" stroke-width="3"/><path d="M26 20 L46 32 L26 44Z" fill="#fff"/></svg></div>
  <div class="spot two" role="img" aria-label="Video still of a voice artist in the studio">
    <svg class="play" viewBox="0 0 64 64"><circle cx="32" cy="32" r="30" fill="rgba(0,0,0,.25)" stroke="#fff" stroke-width="3"/><path d="M26 20 L46 32 L26 44Z" fill="#fff"/></svg></div>
  <div class="spot three" role="img" aria-label="Video still of a voice artist smiling">
    <svg class="play" viewBox="0 0 64 64"><circle cx="32" cy="32" r="30" fill="rgba(0,0,0,.25)" stroke="#fff" stroke-width="3"/><path d="M26 20 L46 32 L26 44Z" fill="#fff"/></svg></div>
</section>
<div class="btn spots-btn">VIEW MORE</div>

<section class="clients">
  <h2 class="section-title">CLIENTS</h2>
  <svg class="arrow" style="left:50px" viewBox="0 0 24 30"><path d="M18 3 L6 15 L18 27" fill="none" stroke="#fff" stroke-width="3"/></svg>
  <div class="logos"><span>Larkfield</span><span><i class="sq"></i>Corvo</span><span>Kestrel</span><span>Brightwater Media</span><span>Hearwell</span></div>
  <svg class="arrow" style="right:50px" viewBox="0 0 24 30"><path d="M6 3 L18 15 L6 27" fill="none" stroke="#fff" stroke-width="3"/></svg>
</section>

<h2 class="section-title news-title">NEWS</h2>
<section class="news">
  <article class="card">
    <div class="card-img a" role="img" aria-label="Black and white portrait of a male voice artist"></div>
    <div class="card-body">
      <div class="meta">By Tarnbelle Voices &nbsp;|&nbsp; May 12, 2023</div>
      <h3>NEW VOICE ALERT | MARCUS PENROSE</h3>
      <p>We are delighted to introduce another great talent to our roster. Marcus brings warm, versatile reads across radio, television and online work, with over twenty years behind the microphone.</p>
    </div>
    <div class="more">READ MORE</div>
  </article>
  <article class="card">
    <div class="card-img b" role="img" aria-label="Portrait of a smiling male voice artist in glasses"></div>
    <div class="card-body">
      <div class="meta">By Tarnbelle Voices &nbsp;|&nbsp; May 11, 2023</div>
      <h3>NEW VOICE ALERT | OLIVER TAMSIN</h3>
      <p>We are pleased to welcome Oliver to the team. A natural storyteller with a friendly, grounded tone, he has voiced national campaigns and narration for many years of experience.</p>
    </div>
    <div class="more">READ MORE</div>
  </article>
</section>
<div class="btn news-btn">VIEW MORE</div>

<section class="testimonials">
  <div class="mic-photo" role="img" aria-label="Studio condenser microphone lit in green"></div>
  <div class="t-body">
    <h2>TESTIMONIALS</h2>
    <blockquote>I've been working with the team at Tarnbelle Voices now for about 11 years and I've always found them to be very professional &amp; personable on all jobs.</blockquote>
    <div class="t-author"><div class="t-badge"></div><div><strong>- DANIEL CROFT</strong><small>Owner - Audio Engineer/Sound Designer</small></div></div>
  </div>
  <div class="t-arrows">
    <span><svg width="12" height="14" viewBox="0 0 12 14"><path d="M9 1 L3 7 L9 13" fill="none" stroke="#fff" stroke-width="2"/></svg></span>
    <span><svg width="12" height="14" viewBox="0 0 12 14"><path d="M3 1 L9 7 L3 13" fill="none" stroke="#fff" stroke-width="2"/></svg></span>
  </div>
</section>

<footer class="footer">
  <div class="f-col" style="left:230px">
    <div class="f-icon"><svg width="22" height="28" viewBox="0 0 22 28"><path d="M11 1C5 1 1 5.5 1 11c0 7 10 16 10 16s10-9 10-16C21 5.5 17 1 11 1z" fill="#fff"/><circle cx="11" cy="11" r="4" fill="#6cbf1f"/></svg></div>
    <div>Tarnbelle Voices Pty Limited<br>Suite 14, 88 Harbour Lane, Marrick<br>NSW 2031 Australia</div>
  </div>
  <div class="f-col" style="left:700px">
    <div class="f-icon"><svg width="24" height="24" viewBox="0 0 24 24"><path d="M5 2h4l2 5-3 2a12 12 0 0 0 7 7l2-3 5 2v4c0 1-1 2-2 2C10 21 3 14 3 4c0-1 1-2 2-2z" fill="#fff"/></svg></div>
    <div>SYDNEY +61 2 9000 4812<br>MELBOURNE +61 3 9000 2367</div>
  </div>
  <div class="f-links">HOME &nbsp;/&nbsp; VOICES &nbsp;/&nbsp; RATES &nbsp;/&nbsp; PAYMENTS &nbsp;/&nbsp; NEWS &nbsp;/&nbsp; ABOUT US &nbsp;/&nbsp; CLIENTS &nbsp;/&nbsp; CONTACT US &nbsp;/&nbsp; SHORTLISTED<br>FAQS &nbsp;/&nbsp; SITEMAP &nbsp;/&nbsp; PRIVACY POLICY &amp; TERMS &amp; CONDITIONS</div>
  <div class="f-copy">© Copyright 2023 Tarnbelle Voices Pty Limited | Privacy Policy &amp; Terms and Conditions | Sitemap</div>
  <div class="to-top"><svg width="12" height="10" viewBox="0 0 12 10"><path d="M1 8 L6 2 L11 8" fill="none" stroke="#fff" stroke-width="2"/></svg></div>
</footer>
</body>
</html>
```